New business card for civil engineering company - "Keystone Audit"

We need a business card designed for our new structural engineering company.

The company name is "Keystone Audit" logo files attached.

We would like the following:
* Two-sided card
* Simple design

Information to be placed on the card:
Name - Marcus Dellow
Job Title - Director / Structural Engineer
Credentials - BEng(Hons), CPEng, CMengNZ, IntPE(NZ)
Email - marcus.dellow@keystoneaudit.co.nz
mobile - 0219364058
website - www.keystoneaudit.co.nz

```html
<!DOCTYPE html>
<html lang="en">
<head>
<meta charset="utf-8">
<title>Keystone Audit – Business Card</title>
<link rel="stylesheet" href="https://fonts.googleapis.com/css2?family=Archivo:wght@400;600;700;800&display=swap">
<style>
  :root {
    --backdrop: #53575a;
    --card: #ffffff;
    --brand-yellow: #ffcc00;
    --brand-blue: #1f3a93;
    --ink: #111111;
    --ink-soft: #2a2a2a;
  }
  * { margin: 0; padding: 0; box-sizing: border-box; }
  html, body {
    width: 1200px;
    height: 1160px;
    overflow: hidden;
    background: var(--backdrop);
    font-family: "Archivo", Arial, sans-serif;
  }
  .canvas { position: relative; width: 1200px; height: 1160px; }
  .card {
    position: absolute;
    left: 182px;
    width: 834px;
    height: 492px;
    background: var(--card);
    box-shadow: 0 4px 10px rgba(0,0,0,0.35);
    overflow: hidden;
  }
  .card--front { top: 69px; }
  .card--back { top: 597px; }
  .brand-square {
    position: absolute;
    background: var(--brand-yellow);
  }
  .brand-name {
    position: absolute;
    color: var(--brand-blue);
    font-weight: 800;
    text-transform: uppercase;
    letter-spacing: 0.04em;
    line-height: 1;
    white-space: nowrap;
  }
  .card--front .brand-square { left: 317px; top: 87px; width: 200px; height: 200px; }
  .card--front .brand-name { left: 0; width: 834px; text-align: center; top: 308px; font-size: 36px; }

  .card--back .brand-square { left: 0; top: 32px; width: 146px; height: 146px; }
  .card--back .brand-name { left: 108px; top: 82px; font-size: 28px; }

  .website {
    position: absolute;
    right: 68px;
    bottom: 32px;
    color: var(--brand-blue);
    font-weight: 700;
    font-size: 23px;
    line-height: 1;
  }
  .corner-square {
    position: absolute;
    right: 0;
    bottom: 10px;
    width: 49px;
    height: 54px;
    background: var(--brand-yellow);
  }
  .contact {
    position: absolute;
    right: 48px;
    top: 64px;
    text-align: right;
    color: var(--brand-blue);
    font-size: 24px;
    line-height: 43px;
  }
  .person {
    position: absolute;
    left: 144px;
    top: 226px;
    color: var(--ink);
  }
  .person__name, .person__role {
    font-weight: 700;
    font-size: 24px;
    line-height: 1;
    margin-bottom: 21px;
  }
  .person__credentials {
    font-weight: 400;
    font-size: 23px;
    color: var(--ink-soft);
    line-height: 1;
    margin-top: 8px;
  }
</style>
</head>
<body>
<main class="canvas">
  <section class="card card--front" aria-label="Card front">
    <div class="brand-square"></div>
    <div class="brand-name">Keystone Audit</div>
    <div class="website">www.keystoneaudit.co.nz</div>
    <div class="corner-square"></div>
  </section>

  <section class="card card--back" aria-label="Card back">
    <div class="brand-square"></div>
    <div class="brand-name">Keystone Audit</div>
    <div class="contact">
      <div class="contact__email">marcus.dellow@keystoneaudit.co.nz</div>
      <div class="contact__phone">0219364058</div>
    </div>
    <div class="person">
      <div class="person__name">Marcus Dellow</div>
      <div class="person__role">Director / Structural Engineer</div>
      <div class="person__credentials">BEng(Hons), CPEng, CMengNZ, IntPE(NZ)</div>
    </div>
    <div class="website">www.keystoneaudit.co.nz</div>
    <div class="corner-square"></div>
  </section>
</main>
</body>
</html>
```